Harborline Frame Construction Needs business card

Hey we are in need of business card designs. I have upload our logo as a guideline, but free feel to run with it or come up with something unique.
Pls have fun with it and be creative. the name says it all!
i will give some directions after i see a few entries..
Logo source file has been uploaded..
Hey because of the logo is so colourful already.
Can we have a few submissions with less colour.
Also we are looking for clever/hidden/descriptive business card.

```html
<!DOCTYPE html>
<html lang="en">
<head>
<meta charset="utf-8">
<title>Harborline Frame Construction – Business Card</title>
<link href="https://fonts.googleapis.com/css2?family=Montserrat:wght@600;700&family=Roboto:wght@400;700&display=swap" rel="stylesheet">
<style>
  :root {
    --stage: #e9e7e4;
    --card: #ffffff;
    --ink: #2b2b2b;
    --brand-grey: #6f6f6f;
    --accent: #2f7fcf;
    --shadow: rgba(0, 0, 0, 0.18);
  }
  * { margin: 0; padding: 0; box-sizing: border-box; }
  html, body {
    width: 1200px;
    height: 913px;
    overflow: hidden;
    background: var(--stage);
  }
  .stage {
    position: relative;
    width: 1200px;
    height: 913px;
  }
  .card {
    position: absolute;
    width: 560px;
    height: 320px;
    background: var(--card);
    box-shadow: 0 10px 28px var(--shadow);
  }
  .card--front { left: 70px; top: 90px; }
  .card--back { left: 570px; top: 500px; }

  .brand {
    display: flex;
    align-items: center;
    gap: 14px;
  }
  .brand__mark {
    width: 34px;
    height: 34px;
    background: var(--accent);
    flex: none;
  }
  .brand__name {
    font-family: "Montserrat", sans-serif;
    font-weight: 700;
    color: var(--brand-grey);
    text-transform: uppercase;
    line-height: 1.1;
  }
  .card--front .brand {
    position: absolute;
    left: 50%;
    top: 50%;
    transform: translate(-50%, -50%);
  }
  .card--front .brand__name { font-size: 30px; }

  .card--back .brand {
    position: absolute;
    left: 36px;
    top: 60px;
    gap: 9px;
  }
  .card--back .brand__mark { width: 18px; height: 18px; }
  .card--back .brand__name { font-size: 15px; }

  .person {
    position: absolute;
    right: 40px;
    top: 46px;
    text-align: right;
    font-family: "Roboto", sans-serif;
    color: var(--ink);
  }
  .person__name { font-size: 19px; font-weight: 400; }
  .person__title { font-size: 11px; margin-top: 2px; }

  .contact {
    position: absolute;
    left: 36px;
    bottom: 34px;
    list-style: none;
    font-family: "Roboto", sans-serif;
    font-weight: 700;
    font-size: 12.5px;
    color: var(--ink);
  }
  .contact__item {
    display: flex;
    align-items: center;
    gap: 10px;
    height: 22px;
  }
  .contact__icon {
    width: 14px;
    height: 14px;
    fill: var(--ink);
    flex: none;
  }
</style>
</head>
<body>
<main class="stage">
  <section class="card card--front" aria-label="Card front">
    <div class="brand">
      <span class="brand__mark"></span>
      <span class="brand__name">Harborline Frame Construction</span>
    </div>
  </section>

  <section class="card card--back" aria-label="Card back">
    <div class="brand">
      <span class="brand__mark"></span>
      <span class="brand__name">Harborline Frame Construction</span>
    </div>

    <div class="person">
      <p class="person__name">Your Name</p>
      <p class="person__title">Title</p>
    </div>

    <ul class="contact">
      <li class="contact__item">
        <svg class="contact__icon" viewBox="0 0 14 14" aria-hidden="true"><path d="M7 0a5 5 0 0 0-5 5c0 3.5 5 9 5 9s5-5.5 5-9a5 5 0 0 0-5-5zm0 7a2 2 0 1 1 0-4 2 2 0 0 1 0 4z"/></svg>
        <span>Your Commercial or office address</span>
      </li>
      <li class="contact__item">
        <svg class="contact__icon" viewBox="0 0 14 14" aria-hidden="true"><path d="M1 4c0-2 1-3 6-3s6 1 6 3v1h-3V4H4v1H1zM3 6h8l2 7H1z"/></svg>
        <span>00.00.00.0000</span>
      </li>
      <li class="contact__item">
        <svg class="contact__icon" viewBox="0 0 14 14" aria-hidden="true"><path d="M3 0h8v4H3zM1 5h12v8H1zm2 2v1h3V7zm0 2v1h3V9zm5-2v4h3V7z"/></svg>
        <span>00.00.00.0000</span>
      </li>
      <li class="contact__item">
        <svg class="contact__icon" viewBox="0 0 14 14" aria-hidden="true"><path d="M0 3h14v1L7 8 0 4zM0 5.2l7 4 7-4V12H0z"/></svg>
        <span>yourname@yourwebsite.com</span>
      </li>
      <li class="contact__item">
        <svg class="contact__icon" viewBox="0 0 14 14" aria-hidden="true"><path d="M7 0a7 7 0 1 0 0 14A7 7 0 0 0 7 0zm-1 1.2C4.8 2.6 4.2 4.5 4.1 6.3H1.3A5.8 5.8 0 0 1 6 1.2zm2 0a5.8 5.8 0 0 1 4.7 5.1H9.9C9.8 4.5 9.2 2.6 8 1.2zM5.3 6.3C5.4 4.6 6 3 7 1.8c1 1.2 1.6 2.8 1.7 4.5zm-4 1.4h2.8c.1 1.8.7 3.7 1.9 5.1a5.8 5.8 0 0 1-4.7-5.1zm4 0h3.4c-.1 1.7-.7 3.3-1.7 4.5-1-1.2-1.6-2.8-1.7-4.5zm4.6 0h2.8A5.8 5.8 0 0 1 8 12.8c1.2-1.4 1.8-3.3 1.9-5.1z"/></svg>
        <span>www.yourwebsite.com</span>
      </li>
    </ul>
  </section>
</main>
</body>
</html>
```